Tech Savy small Business accountant business card design

We need a business card for a new company based in the cloud. We provide tax, business advisory, accounting, information technology solutions and back office functions to small businesses. We offer fixed fee packages with add on services as you need them. By harnessing technology we simplify small business operational processes providing valuable time and information for small business owners to grow their business. In the logo (zulvarine) we want to be able to see zulv and experts. The final design should communicate achieving growth dreams and balance (ie life and $).
Updates
This project has been temporarily placed on hold until I finalize "Tech Savy small Business accountant needs a logo". I invite all designers to submit on this logo project. Once my logo is finalized I will resume this business card contest. Thanks Added Wednesday, March 19, 2014
This project has been temporarily placed on hold until I finalize "Tech Savy small Business accountant logo". I invite all designers to submit on this logo project. Once my logo is finalized I will resume this business card contest. Thanks Added Thursday, March 20, 2014
Target Market(s)
Small Business (Revenue $500,000, more than 3 employees) owners.
Industry/Entity Type
Small Business
Contact Information for Business Card
Marla Pennick (Principal)
Accountant, Tax Agent.
TEL | 0417 583 916
EMAIL | Marla.Pennick@zulvarine.com.au
WEB | www.zulvarine.com.au
Look and feel

```html
<!DOCTYPE html>
<html lang="en">
<head>
<meta charset="utf-8">
<title>zulvarine business card</title>
<link rel="stylesheet" href="https://fonts.googleapis.com/css2?family=Questrial&display=swap">
<style>
  :root {
    --stage: #eceff1;
    --brand-blue: #1fa3d4;
    --brand-blue-deep: #1582b5;
    --brand-blue-light: #3bb9e6;
    --card-white: #ffffff;
    --text-grey: #7d7f82;
    --text-dark: #6a6c70;
  }
  * { margin: 0; padding: 0; box-sizing: border-box; }
  html, body {
    width: 1200px;
    height: 780px;
    overflow: hidden;
    background: var(--stage);
    font-family: "Questrial", sans-serif;
  }
  .canvas {
    width: 1200px;
    height: 780px;
    display: flex;
    align-items: center;
    justify-content: center;
  }
  .business-card {
    position: relative;
    width: 1050px;
    height: 600px;
    overflow: hidden;
    box-shadow: 0 14px 40px rgba(0, 0, 0, 0.18);
  }
  .card-shapes {
    position: absolute;
    inset: 0;
  }
  .brand {
    position: absolute;
    left: 420px;
    top: 160px;
    width: 440px;
  }
  .brand-name {
    font-size: 80px;
    font-weight: 400;
    line-height: 1;
    color: var(--brand-blue);
    letter-spacing: -1px;
  }
  .brand-tagline {
    margin-top: 8px;
    margin-left: 40px;
    font-size: 21px;
    color: var(--text-grey);
    letter-spacing: 0.3px;
    white-space: nowrap;
  }
  .contact {
    position: absolute;
    left: 290px;
    top: 345px;
    color: var(--text-grey);
  }
  .contact-name {
    font-size: 40px;
    font-weight: 400;
    color: var(--brand-blue);
    line-height: 1.1;
  }
  .contact-role {
    font-size: 24px;
    line-height: 1.3;
    color: var(--text-grey);
  }
  .contact-lines {
    list-style: none;
    margin-top: 16px;
  }
  .contact-line {
    display: flex;
    align-items: center;
    gap: 14px;
    font-size: 23px;
    line-height: 1.45;
    color: var(--text-dark);
  }
  .contact-icon {
    width: 28px;
    height: 28px;
    flex: none;
  }
</style>
</head>
<body>
<main class="canvas">
  <article class="business-card">
    <svg class="card-shapes" viewBox="0 0 1050 600" width="1050" height="600" aria-hidden="true">
      <defs>
        <linearGradient id="bandGradient" x1="0" y1="0" x2="1" y2="1">
          <stop offset="0" stop-color="#1582b5"/>
          <stop offset="0.5" stop-color="#1fa3d4"/>
          <stop offset="1" stop-color="#3bb9e6"/>
        </linearGradient>
      </defs>
      <rect width="1050" height="600" fill="url(#bandGradient)"/>
      <path d="M250 0 L770 0 Q1000 300 860 600 L190 600 Q90 330 250 0 Z" fill="#ffffff"/>
    </svg>

    <header class="brand">
      <div class="brand-name">zulvarine</div>
      <div class="brand-tagline">Your business and accounting partner</div>
    </header>

    <section class="contact">
      <h1 class="contact-name">Marla Pennick</h1>
      <p class="contact-role">(Principal)</p>
      <p class="contact-role">Accountant, Tax Agent</p>
      <ul class="contact-lines">
        <li class="contact-line">
          <svg class="contact-icon" viewBox="0 0 28 28" aria-hidden="true">
            <rect width="28" height="28" rx="3" fill="var(--brand-blue)"/>
            <path d="M8 7 h4 l1.5 4 -2.2 1.6 a10 10 0 0 0 4.1 4.1 l1.6-2.2 4 1.5 v4 a2 2 0 0 1-2 2 A15 15 0 0 1 6 9 a2 2 0 0 1 2-2 z" fill="#fff"/>
          </svg>
          0417 583 916
        </li>
        <li class="contact-line">
          <svg class="contact-icon" viewBox="0 0 28 28" aria-hidden="true">
            <rect width="28" height="28" rx="3" fill="var(--brand-blue)"/>
            <rect x="6" y="8.5" width="16" height="11" fill="none" stroke="#fff" stroke-width="1.8"/>
            <path d="M6 8.5 L14 15 L22 8.5" fill="none" stroke="#fff" stroke-width="1.8"/>
          </svg>
          Marla.Pennick@zulvarine.com.au
        </li>
        <li class="contact-line">
          <svg class="contact-icon" viewBox="0 0 28 28" aria-hidden="true">
            <rect width="28" height="28" rx="3" fill="var(--brand-blue)"/>
            <circle cx="14" cy="14" r="8" fill="none" stroke="#fff" stroke-width="1.6"/>
            <ellipse cx="14" cy="14" rx="3.5" ry="8" fill="none" stroke="#fff" stroke-width="1.4"/>
            <path d="M6 14 H22 M7.5 10 H20.5 M7.5 18 H20.5" stroke="#fff" stroke-width="1.3"/>
          </svg>
          www.zulvarine.com.au
        </li>
      </ul>
    </section>
  </article>
</main>
</body>
</html>
```